We need a poster design for "KORVEN Sports Night" events. The events have been around for 3 years and we hope the poster will give a sense of vibrant and active designs. It is more to a community event with teamwork and fun.

I have uploaded a past event poster just FYI.

Target Market(s)

Community, Family

Industry/Entity Type

Non Profit

Logo Text

KORVEN Sports Night

Requirements
Must have
• KORVEN Sports Night
• Organiser: KORVEN Sydney
• Date: 25/11/2017
• Time: 4:00pm
• Venue: Wendilow Park
• Facebook: korvenplay

```html
<!DOCTYPE html>
<html lang="en">
<head>
<meta charset="utf-8">
<title>KORVEN Sports Night Poster</title>
<link rel="stylesheet" href="https://fonts.googleapis.com/css2?family=Russo+One&family=Oswald:wght@500;600&family=Michroma&family=Share+Tech+Mono&family=Montserrat:wght@400;600&display=swap">
<style>
  :root {
    --backdrop: #ececec;
    --paper: #f6eeee;
    --paper-pink: #f4d6d6;
    --red: #ee2a36;
    --red-deep: #c81f2c;
    --red-hot: #ff3b3b;
    --orange: #f7931e;
    --charcoal: #2e2b2c;
    --white: #ffffff;
    --ink: #161616;
    --grey-text: #3a3a3a;
    --plum: #6a2a45;
  }
  html, body {
    margin: 0;
    width: 1200px;
    height: 1200px;
    overflow: hidden;
    background: var(--backdrop);
  }
  .poster {
    position: absolute;
    left: 236px;
    top: 86px;
    width: 728px;
    height: 1028px;
    display: block;
  }
  .paper { fill: url(#paperFade); }
  .red-field { fill: url(#redField); }
  .dark-band { fill: var(--charcoal); }
  .pink-strip { fill: var(--red-hot); opacity: .55; }
  .orange-block { fill: var(--orange); opacity: .75; }
  .athlete-photo { fill: url(#photoTone); }
  .track-stripe { fill: var(--white); opacity: .55; }
  .track-grey { fill: #b9b3b5; opacity: .6; }
  .venue-band { fill: url(#venueFade); }
  .red-shard { fill: var(--red); }
  .red-shard-light { fill: #ff6b6b; opacity: .8; }
  .orange-shard { fill: var(--orange); opacity: .8; }
  .time-label {
    font-family: "Share Tech Mono", monospace;
    fill: var(--white);
    letter-spacing: 6px;
  }
  .time-big {
    font-family: "Share Tech Mono", monospace;
    fill: var(--white);
  }
  .stopwatch { fill: none; stroke: var(--white); stroke-width: 5; }
  .title-main {
    font-family: "Russo One", sans-serif;
    fill: var(--white);
    filter: url(#titleGlow);
  }
  .title-sub {
    font-family: "Oswald", sans-serif;
    font-weight: 600;
    fill: var(--white);
  }
  .organiser-label { font-family: "Michroma", sans-serif; fill: var(--white); }
  .on-box { fill: var(--red); }
  .on-text { font-family: "Russo One", sans-serif; fill: var(--white); }
  .organiser-name { font-family: "Russo One", sans-serif; fill: var(--white); }
  .date-box { fill: var(--white); }
  .date-text { font-family: "Share Tech Mono", monospace; fill: var(--ink); }
  .pin { fill: var(--white); }
  .venue-label { font-family: "Michroma", sans-serif; fill: var(--white); }
  .venue-name { font-family: "Montserrat", sans-serif; font-weight: 400; fill: var(--white); }
  .social-dot { fill: #8d8fb0; }
  .social-name {
    font-family: "Montserrat", sans-serif;
    font-weight: 400;
    fill: var(--grey-text);
    letter-spacing: 9px;
  }
</style>
</head>
<body>
<svg class="poster" viewBox="0 0 910 1285" xmlns="http://www.w3.org/2000/svg" role="img" aria-label="KORVEN Sports Night poster">
  <defs>
    <linearGradient id="paperFade" x1="0" y1="0" x2="0" y2="1">
      <stop offset="0" stop-color="var(--paper)"/>
      <stop offset=".35" stop-color="var(--paper-pink)"/>
      <stop offset=".75" stop-color="#f2c9c9"/>
      <stop offset="1" stop-color="#f0e8e8"/>
    </linearGradient>
    <linearGradient id="redField" x1="0" y1="0" x2="1" y2="1">
      <stop offset="0" stop-color="var(--red-hot)"/>
      <stop offset=".5" stop-color="var(--red)"/>
      <stop offset="1" stop-color="var(--red-deep)"/>
    </linearGradient>
    <linearGradient id="photoTone" x1="0" y1="0" x2="1" y2="1">
      <stop offset="0" stop-color="#efe6f0"/>
      <stop offset=".35" stop-color="#b993b8"/>
      <stop offset=".7" stop-color="var(--plum)"/>
      <stop offset="1" stop-color="#d0424e"/>
    </linearGradient>
    <linearGradient id="venueFade" x1="0" y1="0" x2="1" y2="0">
      <stop offset="0" stop-color="#3e3336" stop-opacity=".92"/>
      <stop offset=".6" stop-color="#6d5d60" stop-opacity=".7"/>
      <stop offset="1" stop-color="#9a8e90" stop-opacity=".2"/>
    </linearGradient>
    <filter id="titleGlow" x="-20%" y="-40%" width="140%" height="180%">
      <feDropShadow dx="0" dy="0" stdDeviation="6" flood-color="#ffc247" flood-opacity=".9"/>
    </filter>
  </defs>

  <!-- base and colour fields -->
  <rect class="paper" width="910" height="1285"/>
  <polygon class="red-field" points="380,275 910,95 910,900 0,900 0,380"/>
  <polygon class="orange-block" points="460,470 820,455 820,560 470,575"/>

  <!-- athlete photo area -->
  <polygon class="athlete-photo" points="0,360 300,300 470,330 520,470 640,860 0,870" role="img" aria-label="Photo of a sprinter in a white long-sleeve top crouched in the starting position on a running track"/>

  <!-- time band -->
  <polygon class="dark-band" points="0,207 418,57 418,197 0,300"/>
  <polygon class="pink-strip" points="0,300 445,192 445,215 0,325"/>
  <text class="time-label" transform="translate(82,222) rotate(-19)" font-size="30">BE THERE BY</text>
  <text class="time-big" transform="translate(84,284) rotate(-19)" font-size="74" textLength="275" lengthAdjust="spacingAndGlyphs">4:00PM</text>
  <g class="stopwatch">
    <circle cx="43" cy="262" r="22"/>
    <line x1="43" y1="240" x2="43" y2="228"/>
    <line x1="43" y1="262" x2="43" y2="250"/>
  </g>

  <!-- title band -->
  <polygon class="dark-band" points="470,265 910,165 910,395 460,450"/>
  <text class="title-main" transform="translate(505,338) rotate(-9)" font-size="112" textLength="370" lengthAdjust="spacingAndGlyphs">KORVEN</text>
  <text class="title-sub" transform="translate(476,418) rotate(-7)" font-size="66" textLength="395" lengthAdjust="spacingAndGlyphs">SPORTS NIGHT</text>

  <!-- track lines -->
  <polygon class="track-grey" points="0,880 910,850 910,880 0,910"/>
  <polygon class="track-stripe" points="300,915 910,905 910,930 300,940"/>
  <polygon class="track-stripe" points="0,960 910,930 910,945 0,975"/>

  <!-- organiser block -->
  <rect class="dark-band" x="563" y="510" width="322" height="117"/>
  <text class="organiser-label" x="865" y="575" font-size="40" text-anchor="end" textLength="235" lengthAdjust="spacingAndGlyphs">ORGANISER</text>
  <rect class="on-box" x="508" y="572" width="104" height="65"/>
  <text class="on-text" x="560" y="622" font-size="44" text-anchor="middle">ON</text>
  <text class="organiser-name" x="628" y="618" font-size="32" textLength="250" lengthAdjust="spacingAndGlyphs">KORVEN SYDNEY</text>
  <rect class="date-box" x="563" y="629" width="347" height="88"/>
  <text class="date-text" x="580" y="702" font-size="76" textLength="270" lengthAdjust="spacingAndGlyphs">25.11.2017</text>

  <!-- venue -->
  <polygon class="venue-band" points="0,935 910,885 910,1078 0,1078"/>
  <path class="pin" d="M90 945 a35 35 0 0 1 35 35 c0 25 -35 70 -35 70 c0 0 -35 -45 -35 -70 a35 35 0 0 1 35 -35 z M90 965 a15 15 0 1 0 0.01 0 z" fill-rule="evenodd"/>
  <text class="venue-label" x="156" y="995" font-size="54" textLength="320" lengthAdjust="spacingAndGlyphs">VENUE</text>
  <text class="venue-name" x="156" y="1048" font-size="38">WENDILOW PARK</text>

  <!-- social -->
  <circle class="social-dot" cx="85" cy="1135" r="30"/>
  <text class="social-name" x="150" y="1148" font-size="38">KORVENPLAY</text>

  <!-- bottom shards -->
  <polygon class="red-shard" points="500,1100 910,1285 690,1285"/>
  <polygon class="red-shard-light" points="640,1150 910,1140 910,1200"/>
  <polygon class="red-shard" points="0,1175 330,1285 0,1285"/>
  <polygon class="orange-shard" points="220,1285 560,1210 480,1285"/>
  <polygon class="red-shard-light" points="380,1285 700,1240 620,1285"/>
</svg>
</body>
</html>
```